Verpackungsdesign für Dattelkernpulver gesucht
Zielgruppe
Zu uns: Wir sind Nuvo-Lind. Mit unserem Dattelkernpulver bieten wir jedem die Chance die Power der Dattelkerne aktiver in die Ernährung zu integrieren. Neugierigen sowie auch Dattelkennern helfen wir eine ausgewogene Ernährung zu erreichen – dank der sagenumwobenen gesundheitlichen Vorteile der Ajwa-Dattel aus dem Orient. 100% naturbelassen, nicht wärmebehandelt und aus unserer Überzeugung für eine gesunde Ernährung.
Zur Zielgruppe: 50% w/50% m, 30+, aus Deutschland, progressiv und leicht esoterisch, mittleres-höheres Einkommenslevel (EUR 45k+), tendenziell höherer Bildungsgrad, typischerweise 'Verdalis'-Sympathisanten
Aufgabenstellung
Allgemein: Das Produktetikett wird um ein kleines 150g-200g Glas herum angebracht und auf den Deckel ebenfalls ein Rundes Etikett angebracht – verbunden durch ein “Siegel” mit dem zuvorgenannten Hauptetikett.
Vorderseite: Eindeutig erkennbares Logo und Markenname. Auf ersten Blick zu erkennen, dass es sich um Dattelkernpulver handelt ('Dattelkernpulver') inkl. einer Illustration die das leicht erkennen lässt. Deutliche Symbolik: 'Vegan', 'Laktosefrei', “ohne Konservierungsstoffe”, 'Ungezuckert', “Hergestellt in Deutschland”
Seite: Kleiner Blocktext mit 3-4 Zeilen mit kurzer Story zu unserer Überzeugung ('Die Power-Frucht aus 1001 Nacht: Dattelkernpulver von sorgfältig ausgewählten Premium Ajwa-Datteln aus Medina. 100% naturbelassen, nicht wärmebehandelt und aus unserer Überzeugung für ein gesundes Leben.') Zusätzlich eine Verzehrempfehlung ('Als täglicher Begleiter Deiner gesunden Ernährung je morgens einen Teelöffel.')
Rückseite: sehr leicht aufzufindende Zutatenliste sowie ein Dummy für die Nährwerttabelle. Kleiner Hinweis weiter unten auf Rückseite zur Marke (ähnlich wie private label 'kp Hausqualität') mit Kontaktdaten (Webseite, Email, Standort), dass unsere Transparenz und Erreichbarkeit vermittelt.
Oberseite: Label geht mit 'Siegel' bis auf den runden Deckel. Auf Oberseite Logo und schnell identifizierbarer Produktname.
Bitte beachten: Keine Kreuze, keine Dreiecke, nicht zu verspielt.
** Vielen Dank - ich freue mich auf Deinen spannenden Vorschlag! **
Maße:
-> Label: Breite 230mm, Höhe 30mm
-> Deckel: 50mm Druchmesser
-> Lasche vom Deckel zum Label: Breite ca. 10mm-15mm

```html
<!DOCTYPE html>
<html lang="de">
<head>
<meta charset="utf-8">
<title>Nuvo-Lind Dattelkernpulver – Etikett</title>
<link rel="stylesheet" href="https://fonts.googleapis.com/css2?family=Arimo:wght@400;700&family=Courgette&family=Noto+Serif:ital,wght@1,400;1,700&display=swap">
<style>
  :root{
    --green:#9cc33a;
    --green-dark:#4f8a1c;
    --green-text:#3f6f17;
    --blue:#2a8fce;
    --label-bg:#eef1f3;
    --white:#ffffff;
    --ink:#2f4a1a;
    --bg-dark:#555557;
    --bg-light:#9a9a9b;
    --date-dark:#2e1a12;
    --date-mid:#6b3a22;
  }
  *{box-sizing:border-box;margin:0;padding:0}
  html,body{width:1200px;height:2449px;overflow:hidden}
  body{font-family:"Arimo",Arial,sans-serif;color:var(--ink)}
  .canvas{position:relative;width:1200px;height:2449px;overflow:hidden}
  .board{position:absolute;left:0;width:1200px}
  .board--top{top:0;height:1346px;background:radial-gradient(ellipse at 50% 95%,var(--bg-light) 0%,#7d7d7e 40%,var(--bg-dark) 100%)}
  .board--bottom{top:1346px;height:1103px;background:radial-gradient(ellipse at 50% 45%,var(--bg-light) 0%,#7a7a7b 45%,var(--bg-dark) 100%)}

  .sticker{position:absolute}
  .sticker text{font-family:"Arimo",Arial,sans-serif}

  .label{position:absolute;left:88px;top:440px;width:952px;height:124px;background:var(--label-bg);border-top:4px solid var(--green)}
  .panel{position:absolute;top:0;height:100%}
  .panel--back{left:0;width:267px}
  .panel--front{left:267px;width:420px;background:linear-gradient(180deg,#f7f8f9 0%,#e3e6e8 100%);overflow:hidden}
  .panel--side{left:687px;width:265px}

  .ingredients{position:absolute;left:12px;top:14px;width:164px;font-size:8px;line-height:10px;color:var(--ink)}
  .ingredients h3{font-size:10px;font-weight:700;margin-bottom:2px}
  .ingredients .origin{font-weight:700;margin-top:5px;font-size:8.5px}
  .ingredients .divider{border-top:1px dashed #6b7a5e;margin:7px 0 0;width:155px}
  .contact{position:absolute;left:12px;top:84px;font-size:8px;line-height:8.5px;color:var(--ink);display:flex;gap:16px}

  .nutrition{position:absolute;left:181px;top:8px;width:73px;height:106px;background:var(--green);padding:3px}
  .nutrition__inner{border:1px solid #e6f1c9;height:100%;padding:3px 4px;color:#2d4a12;font-size:3.6px;line-height:5px}
  .nutrition h4{font-size:7px;line-height:8px;font-weight:700;border-bottom:1px solid #2d4a12;margin-bottom:2px}
  .nutrition .row{display:flex;justify-content:space-between;border-bottom:.5px solid #4d6d22}

  .brand{position:absolute;left:22px;top:20px;display:flex;align-items:center;gap:8px}
  .brand__dot{width:22px;height:22px;border-radius:50%;background:var(--blue)}
  .brand__name{font-size:17px;font-weight:700;color:var(--green-text);line-height:17px}
  .swoosh{position:absolute;left:0;top:0}
  .claim{position:absolute;right:12px;top:8px;text-align:right;font-family:"Noto Serif",Georgia,serif;font-style:italic;font-size:11px;line-height:14px;color:var(--green-text)}
  .title{position:absolute;left:20px;top:78px;font-family:"Courgette",cursive;font-size:21px;line-height:26px;color:var(--green-dark)}
  .photo{position:absolute;left:214px;top:44px;width:132px;height:72px;border-radius:40px 40px 46px 46px;background:radial-gradient(ellipse at 45% 40%,var(--date-mid) 0%,var(--date-dark) 70%,#8f8f8f 100%)}
  .badge-orient{position:absolute;left:342px;top:46px;width:54px;height:54px;border-radius:50%;background:var(--blue);border:3px solid #cfe6f5;color:var(--white);text-align:center;font-weight:700;padding-top:11px;font-size:9px;line-height:11px}
  .badge-orient strong{display:block;font-size:14px;line-height:15px}
  .weight{position:absolute;left:372px;top:100px;font-size:14px;line-height:16px;font-weight:700;color:var(--green-text)}

  .story{position:absolute;left:13px;top:13px;width:245px;height:52px;background:var(--green);padding:4px 7px;color:var(--white);font-size:5.4px;line-height:6.6px;overflow:hidden}
  .story h5{font-size:7.5px;line-height:9px;font-weight:700;color:#2d4a12}
  .symbols{position:absolute;left:54px;top:80px;display:flex;gap:12px}
  .symbol{width:31px;height:31px;border-radius:50%;border:2px solid var(--blue);background:var(--white);position:relative}
  .symbol::after{content:"";position:absolute;inset:5px;border-radius:50%;background:var(--blue);opacity:.85}
</style>
</head>
<body>
<div class="canvas">
  <section class="board board--top">

    <svg class="sticker" style="left:454px;top:84px" width="220" height="360" viewBox="0 0 220 360" aria-label="Deckeletikett mit Lasche">
      <rect x="80" y="190" width="62" height="170" fill="var(--green)"/>
      <circle cx="110" cy="110" r="103" fill="var(--green)"/>
      <circle cx="110" cy="110" r="89" fill="none" stroke="var(--white)" stroke-width="4"/>
      <text x="110" y="117" text-anchor="middle" font-size="20" font-weight="700" fill="var(--white)">Nuvo-Lind</text>
    </svg>

    <svg class="sticker" style="left:683px;top:90px" width="206" height="206" viewBox="0 0 240 240" aria-label="Rundetikett weiß">
      <defs>
        <path id="arcTopA" d="M44,120 A76,76 0 0 1 196,120"/>
        <path id="arcBotA" d="M30,120 A90,90 0 0 0 210,120"/>
      </defs>
      <circle cx="120" cy="120" r="119" fill="var(--white)"/>
      <circle cx="120" cy="120" r="106" fill="none" stroke="var(--green)" stroke-width="4"/>
      <text font-size="21" fill="var(--green)"><textPath href="#arcTopA" startOffset="50%" text-anchor="middle">Dattelkernpulver</textPath></text>
      <text font-size="21" fill="var(--green)" dy="-4"><textPath href="#arcBotA" startOffset="50%" text-anchor="middle">Premium Ajwa</textPath></text>
      <text x="120" y="127" text-anchor="middle" font-size="20" font-weight="700" fill="var(--green)">Nuvo-Lind</text>
    </svg>

    <svg class="sticker" style="left:905px;top:90px" width="206" height="206" viewBox="0 0 240 240" aria-label="Rundetikett grün">
      <defs>
        <path id="arcTopB" d="M44,120 A76,76 0 0 1 196,120"/>
        <path id="arcBotB" d="M30,120 A90,90 0 0 0 210,120"/>
      </defs>
      <circle cx="120" cy="120" r="119" fill="var(--green)"/>
      <circle cx="120" cy="120" r="106" fill="none" stroke="var(--white)" stroke-width="4"/>
      <text font-size="21" fill="var(--white)"><textPath href="#arcTopB" startOffset="50%" text-anchor="middle">Dattelkernpulver</textPath></text>
      <text font-size="21" fill="var(--white)" dy="-4"><textPath href="#arcBotB" startOffset="50%" text-anchor="middle">Premium Ajwa</textPath></text>
      <text x="120" y="129" text-anchor="middle" font-size="26" font-weight="700" fill="var(--white)">Nuvo-Lind</text>
    </svg>

    <div class="label">
      <div class="panel panel--back">
        <div class="ingredients">
          <h3>Zutaten :</h3>
          <p>Vegan, Laktosefrei,<br>Ohne Konservierungsstoffe, Ungezuckert,</p>
          <p class="origin">Ursprung : Deutschland</p>
          <div class="divider"></div>
        </div>
        <div class="contact">
          <p>your place<br>zip code<br>country</p>
          <p>www.yourwebsite.com<br>yourmail@.com</p>
        </div>
        <div class="nutrition">
          <div class="nutrition__inner">
            <h4>Nutrition Facts</h4>
            <div class="row"><span>Serving Size</span><span>5 g</span></div>
            <div class="row"><span>Servings</span><span>40</span></div>
            <div class="row"><span>Amount Per Serving</span><span></span></div>
            <div class="row"><span>Calories</span><span>0</span></div>
            <div class="row"><span>Fat</span><span>0 g</span></div>
            <div class="row"><span>Carbohydrate</span><span>0 g</span></div>
            <div class="row"><span>Sugars</span><span>0 g</span></div>
            <div class="row"><span>Fiber</span><span>0 g</span></div>
            <div class="row"><span>Protein</span><span>0 g</span></div>
            <div class="row"><span>Salt</span><span>0 g</span></div>
          </div>
        </div>
      </div>

      <div class="panel panel--front">
        <svg class="swoosh" width="420" height="120" viewBox="0 0 420 120" aria-hidden="true">
          <path d="M250,40 C285,30 290,4 320,2 L420,2 L420,40 Z" fill="var(--green)"/>
          <path d="M0,55 C120,70 230,58 290,26 C250,62 130,74 0,58 Z" fill="#b8bcbf"/>
          <path d="M0,58 C120,72 220,64 260,44 C220,70 120,78 0,62 Z" fill="var(--green)"/>
        </svg>
        <div class="brand">
          <span class="brand__dot"></span>
          <span class="brand__name">Nuvo-Lind</span>
        </div>
        <p class="claim">Gesunde Ernährung<br>Premium Ajwa</p>
        <p class="title">Dattelkernpulver</p>
        <div class="photo" role="img" aria-label="Foto: Ajwa-Datteln auf einer Schale"></div>
        <div class="badge-orient">Orient.<strong>100%</strong></div>
        <p class="weight">200 g</p>
      </div>

      <div class="panel panel--side">
        <div class="story">
          <h5>Die Power-Frucht aus 1001 Nacht:</h5>
          <p>Dattelkernpulver von sorgfältig ausgewählten Premium Ajwa-Datteln aus Medina. 100% naturbelassen, nicht wärmebehandelt und aus unserer Überzeugung für ein gesundes Leben. Zusätzlich eine Verzehrempfehlung (Als täglicher Begleiter Deiner gesunden Ernährung je morgens einen Teelöffel.)</p>
        </div>
        <div class="symbols">
          <span class="symbol" role="img" aria-label="Symbol Vegan"></span>
          <span class="symbol" role="img" aria-label="Symbol Laktosefrei"></span>
          <span class="symbol" role="img" aria-label="Symbol ohne Konservierungsstoffe"></span>
          <span class="symbol" role="img" aria-label="Symbol Ungezuckert"></span>
        </div>
      </div>
    </div>
  </section>

  <section class="board board--bottom">
    <svg class="sticker" style="left:178px;top:132px" width="156" height="236" viewBox="0 0 156 236" aria-label="Deckeletikett Variante weiß">
      <defs>
        <path id="arcTopC" d="M28,78 A50,50 0 0 1 128,78"/>
        <path id="arcBotC" d="M18,78 A60,60 0 0 0 138,78"/>
      </defs>
      <rect x="54" y="120" width="48" height="116" fill="var(--white)"/>
      <circle cx="78" cy="78" r="77" fill="var(--white)"/>
      <circle cx="78" cy="78" r="68" fill="none" stroke="var(--green)" stroke-width="3"/>
      <text font-size="13" fill="var(--green)"><textPath href="#arcTopC" startOffset="50%" text-anchor="middle">Dattelkernpulver</textPath></text>
      <text font-size="13" fill="var(--green)" dy="-3"><textPath href="#arcBotC" startOffset="50%" text-anchor="middle">Premium Ajwa</textPath></text>
      <text x="78" y="83" text-anchor="middle" font-size="13" font-weight="700" fill="var(--green)">Nuvo-Lind</text>
    </svg>

    <svg class="sticker" style="left:522px;top:132px" width="156" height="236" viewBox="0 0 156 236" aria-label="Deckeletikett Variante grün">
      <rect x="54" y="120" width="48" height="116" fill="var(--green)"/>
      <circle cx="78" cy="78" r="77" fill="var(--green)"/>
      <circle cx="78" cy="78" r="66" fill="none" stroke="var(--white)" stroke-width="3"/>
      <text x="78" y="83" text-anchor="middle" font-size="14" font-weight="700" fill="var(--white)">Nuvo-Lind</text>
    </svg>

    <svg class="sticker" style="left:866px;top:132px" width="156" height="236" viewBox="0 0 156 236" aria-label="Deckeletikett Variante grün mit Marke">
      <defs>
        <path id="arcTopD" d="M28,78 A50,50 0 0 1 128,78"/>
        <path id="arcBotD" d="M18,78 A60,60 0 0 0 138,78"/>
      </defs>
      <rect x="54" y="120" width="48" height="116" fill="var(--green)"/>
      <circle cx="78" cy="78" r="77" fill="var(--green)"/>
      <circle cx="78" cy="78" r="68" fill="none" stroke="var(--white)" stroke-width="3"/>
      <text font-size="13" fill="var(--white)"><textPath href="#arcTopD" startOffset="50%" text-anchor="middle">Dattelkernpulver</textPath></text>
      <text font-size="13" fill="var(--white)" dy="-3"><textPath href="#arcBotD" startOffset="50%" text-anchor="middle">Premium Ajwa</textPath></text>
      <text x="78" y="84" text-anchor="middle" font-size="17" font-weight="700" fill="var(--white)">Nuvo-Lind</text>
    </svg>
  </section>
</div>
</body>
</html>
```